New Meal Prep Flyer for New Package Deals

We are looking for a design that displays our new packages that we offer. If you take a look at our website www.brambleforkmeals.com, and click on packages , you'll see the way we display them currently . We would like something similar to that in style . The first package is called "Horizon" and this package will be a 1 week package (7 days ), 2 meals a day, for a price of $195.00. The second package is called "Amber" and this package will be a 3 week package (21 days) 2 meals per day, for a price of $546.00 , the third package is a 6 week+ package (45 days), and it is called "Evergreen" , 2 meals per day , and the price is $1080.00 .
For the Amber Package , can you put next to it "Save $42.00!"
For the Evergreen Package, can you put next to it "Save $180!"
We also want our logo on the flyer (see attached), and we are just looking for a 1 page flyer , 8 1/2 x 11.

```html
<!DOCTYPE html>
<html lang="en">
<head>
<meta charset="utf-8">
<title>Bramblefork Meals – New Packages Flyer</title>
<link href="https://fonts.googleapis.com/css2?family=Montserrat:wght@500;600;700;800&family=Roboto+Condensed:wght@700&display=swap" rel="stylesheet">
<style>
  :root{
    --stage:#2f2f2f;
    --paper:#f7f7f6;
    --green:#95c11f;
    --ink:#111111;
    --grey:#6a6a6a;
    --logo-grey:#8e8e8e;
    --orange-a:#e8952a;
    --orange-b:#b45f14;
    --gold-a:#e4b23c;
    --gold-b:#b8781c;
    --tab-dark:#3c3c3c;
  }
  *{box-sizing:border-box;margin:0;padding:0}
  html,body{width:1200px;height:1200px;overflow:hidden;background:var(--stage)}
  body{position:relative;font-family:"Montserrat",sans-serif}
  .flyer{position:absolute;left:209px;top:93px;width:784px;height:1016px;background:var(--paper);overflow:hidden}
  .doodle-pattern{position:absolute;inset:0;background:radial-gradient(circle at 50% 40%,#fbfbfb,#ededed)}
  .abs{position:absolute}
  .accent-tick{left:112px;top:12px;width:2px;height:33px;background:var(--green)}
  .brand-name{left:0;width:784px;top:50px;text-align:center;font-weight:800;font-size:64px;letter-spacing:1px;color:var(--logo-grey);line-height:1}
  .brand-tagline{left:0;width:784px;top:136px;text-align:center;font-family:"Roboto Condensed",sans-serif;font-weight:700;font-size:30px;color:var(--green);line-height:1;word-spacing:2px}
  .brand-tagline .divider{display:inline-block;width:2px;height:30px;background:var(--green);vertical-align:-4px;margin:0 14px}
  .packages-header{left:25px;top:194px;width:736px;height:102px;background:var(--green);border-radius:60px 60px 0 0;color:#fff;font-weight:800;font-size:50px;text-align:center;line-height:108px;letter-spacing:.5px}
  .packages-table{left:25px;top:294px;width:736px;height:418px;border:3px solid var(--green);border-top:none}
  .row-rule{left:49px;width:634px;height:2px;background:var(--green)}
  .pkg-name{left:91px;font-weight:800;font-size:33px;line-height:1}
  .pkg-price{left:91px;font-weight:800;font-size:31px;line-height:1}
  .tone-orange{background:linear-gradient(180deg,var(--orange-a),var(--orange-b));-webkit-background-clip:text;background-clip:text;color:transparent}
  .tone-grey{color:var(--grey)}
  .tone-gold{background:linear-gradient(180deg,var(--gold-a),var(--gold-b));-webkit-background-clip:text;background-clip:text;color:transparent}
  .pkg-bar{left:321px;width:3px;background:var(--green)}
  .pkg-detail{font-size:22px;line-height:1;color:var(--grey);font-weight:500;white-space:nowrap}
  .pkg-detail em{font-style:normal;color:var(--green)}
  .pkg-meals{font-size:22px;line-height:1;color:var(--green);font-weight:700;white-space:nowrap}
  .save-tab{left:725px;width:34px;border-radius:8px 0 0 8px;display:flex;align-items:center;justify-content:center}
  .save-tab span,.save-label{writing-mode:vertical-rl;transform:rotate(180deg);font-family:"Roboto Condensed",sans-serif;font-weight:700;white-space:nowrap}
  .save-tab span{color:#fff;font-size:21px}
  .save-tab.dark{top:448px;height:100px;background:linear-gradient(90deg,#6b6b6b,var(--tab-dark))}
  .save-tab.gold{top:559px;height:103px;background:linear-gradient(90deg,var(--gold-a),var(--gold-b))}
  .save-label{font-size:20px}
  .save-label.dark{left:702px;top:470px;color:var(--grey)}
  .save-label.gold{left:702px;top:582px;color:#d59b27}
  .order-line{left:0;width:784px;top:730px;text-align:center;font-weight:700;font-size:23px;color:var(--ink)}
  .contact-row{left:0;top:775px;width:784px;height:30px}
  .globe{left:94px;top:8px}
  .site-url{left:115px;top:3px;font-weight:700;font-size:18px;color:var(--ink)}
  .contact-divider{left:402px;top:2px;width:2px;height:26px;background:var(--ink)}
  .store-badge{top:0;width:105px;height:29px;background:#2a2a2a;border-radius:5px}
  .food-photo{left:0;top:812px;width:784px;height:204px;background:linear-gradient(180deg,rgba(247,247,246,1) 0%,rgba(220,200,150,.6) 28%,#7aa644 55%,#e88a2e 78%,#c9473a 100%)}
</style>
</head>
<body>
<main class="flyer">
  <div class="doodle-pattern" role="img" aria-label="Faint line-drawn pattern of vegetables across the background"></div>

  <div class="abs accent-tick"></div>
  <h1 class="abs brand-name">BRAMBLEFORK</h1>
  <p class="abs brand-tagline">HEALTHY KITCHEN<span class="divider"></span>MEAL PREP</p>

  <h2 class="abs packages-header">OUR NEW PACKAGES</h2>
  <div class="abs packages-table"></div>
  <div class="abs row-rule" style="top:437px"></div>
  <div class="abs row-rule" style="top:575px"></div>

  <!-- Horizon -->
  <div class="abs pkg-name tone-orange" style="top:342px">Horizon</div>
  <div class="abs pkg-price tone-orange" style="top:389px">$195.00</div>
  <div class="abs pkg-bar" style="top:335px;height:68px"></div>
  <div class="abs pkg-detail" style="left:358px;top:341px">1 week package <em>(7 days )</em></div>
  <div class="abs pkg-meals" style="left:358px;top:375px">2 meals a day</div>

  <!-- Amber -->
  <div class="abs pkg-name tone-grey" style="top:473px">Amber</div>
  <div class="abs pkg-price tone-grey" style="top:518px">$546.00</div>
  <div class="abs pkg-bar" style="top:481px;height:65px"></div>
  <div class="abs pkg-detail" style="left:352px;top:483px">3 week package <em>(21 days)</em></div>
  <div class="abs pkg-meals" style="left:352px;top:517px">2 meals per day</div>
  <div class="abs save-label dark">Save</div>
  <div class="abs save-tab dark"><span>$42.00!</span></div>

  <!-- Evergreen -->
  <div class="abs pkg-name tone-gold" style="top:605px">Evergreen</div>
  <div class="abs pkg-price tone-gold" style="top:645px">$1080.00</div>
  <div class="abs pkg-bar" style="top:601px;height:66px"></div>
  <div class="abs pkg-detail" style="left:352px;top:620px">6 week package <em>(45 days)</em></div>
  <div class="abs pkg-meals" style="left:352px;top:650px">2 meals per day</div>
  <div class="abs save-label gold">Save</div>
  <div class="abs save-tab gold"><span>$180.00!</span></div>

  <p class="abs order-line">Order Food easily on our APP or visit our website</p>
  <div class="abs contact-row">
    <svg class="abs globe" width="13" height="13" viewBox="0 0 24 24" fill="none" stroke="#111" stroke-width="2.4">
      <circle cx="12" cy="12" r="10"/><path d="M2 12h20M12 2c3 3 3 17 0 20M12 2c-3 3-3 17 0 20"/>
    </svg>
    <span class="abs site-url">www.brambleforkmeals.com</span>
    <div class="abs contact-divider"></div>
    <div class="abs store-badge" style="left:421px"></div>
    <div class="abs store-badge" style="left:535px"></div>
  </div>

  <div class="abs food-photo" role="img" aria-label="Photo of fresh healthy ingredients: greens, citrus, avocado, tomatoes, nuts, berries, raw meat, salmon and bananas"></div>
</main>
</body>
</html>
```